Harbor Learning Center Posters Showing Building Blocks

We need poster designs for a School in Arizona for kids with Autism. There will be 4 such posters needed which highlight our schools building blocks. Requirements for all 4 posters are as followed: 1) We need the Harbor Learning Center Logo on each poster. I have included attachment. 2) The posters need the following titles: Building Block #1 (for the first poster), Building Block #2 for the 2nd poster, Building Block #3 for the 3rd poster, and Building Block #4 for the forth poster. 3) The main text and focus of the posters will be the following key words: For the first poster the words "Kids first in every decision". The words for the second poster are: "Students are friends with each other, and welcome new students with open arms." The words for the 3rd poster are: "The school is quiet, and students are working hard to do their best." The words for the 4th poster are: "Parents see amazing improvement in their child." 4) We would love to use some of the kids art from our schools if possible. Use your expertise to decide. I will send these out as well. 5) Try and design the posters around the key words from each poster 6) I am sure if landscape or portrait would be best so I will let the experts decide. All 4 posters need to be the same layout once decided.

Target Market(s)

These posters are for the school only. Prospective students/parents will see these posters so they will be used for Marketing from that perspective. We may put out into local community in future.

Industry/Entity Type

School

Font styles to use
Serif

Requirements
Must have
• 1) Logo (Harbor Learning Center for Growth and Discovery)
• 2) Title: as described in write up
• 3) Key words: as described in write up
Nice to have
• Kids art from school. Note: This is the first time that I have been on this site so I may have made a mistake by putting 4 posters on one project. I am assuming that I would need to pay more to have 4 posters so let me know if I need to modify the project in any way?

```html
<!DOCTYPE html>
<html lang="en">
<head>
<meta charset="utf-8">
<title>Harbor Learning Center – Building Block #2</title>
<link rel="stylesheet" href="https://fonts.googleapis.com/css2?family=Libre+Baskerville:wght@700&family=Tinos:wght@400&family=Sniglet:wght@800&display=swap">
<style>
  :root {
    --badge-blue: #1e88d6;
    --badge-red: #e2131d;
    --badge-yellow: #fff200;
    --ink: #1a1a1a;
    --rule-red: #e2131d;
    --line-yellow: #ffee1c;
    --line-blue: #33a7e8;
    --line-red: #e8141c;
    --paper: #f6ecf4;
  }
  * { margin: 0; padding: 0; box-sizing: border-box; }
  html, body { width: 848px; height: 1200px; overflow: hidden; background: #fff; }
  .poster {
    position: relative;
    width: 848px;
    height: 1200px;
    overflow: hidden;
    background: var(--paper);
  }
  .wash {
    position: absolute;
    inset: 0;
    background:
      radial-gradient(ellipse 240px 300px at 800px 760px, rgba(240,60,20,.95), transparent 72%),
      radial-gradient(ellipse 200px 200px at 820px 940px, rgba(250,190,40,.9), transparent 70%),
      radial-gradient(ellipse 220px 220px at 780px 1160px, rgba(70,190,80,.85), transparent 70%),
      radial-gradient(ellipse 260px 320px at 60px 860px, rgba(200,50,200,.9), transparent 72%),
      radial-gradient(ellipse 160px 90px at 580px 520px, rgba(225,70,150,.55), transparent 70%),
      radial-gradient(ellipse 220px 120px at 160px 520px, rgba(210,120,210,.45), transparent 70%),
      linear-gradient(180deg, #f8eef6 0%, #f4dcef 30%, #efc6e6 40%, #e2a0d8 50%, #c05fce 62%, #7d3fcf 78%, #4a36cc 100%);
  }
  .heart-art {
    position: absolute;
    left: 150px;
    top: 600px;
    width: 500px;
    height: 580px;
    border-radius: 48% 48% 40% 40%;
    background:
      radial-gradient(ellipse 120px 130px at 50% 42%, #5fb0f0 0%, #2b6fe0 60%, transparent 100%),
      radial-gradient(ellipse 250px 290px at 50% 45%, #1f3fd4 0%, #2a55e0 55%, rgba(60,160,235,.9) 78%, transparent 100%);
  }
  .badge {
    position: absolute;
    top: 0;
    right: 0;
    display: flex;
    height: 62px;
    font-family: "Libre Baskerville", serif;
    font-weight: 700;
    font-size: 38px;
    line-height: 62px;
  }
  .badge span { display: block; text-align: center; }
  .badge .word-building { background: var(--badge-blue); color: #fff; width: 204px; }
  .badge .word-block { background: var(--badge-red); color: #fff; width: 143px; }
  .badge .word-number { background: var(--badge-yellow); color: var(--badge-red); width: 67px; }
  .brand {
    position: absolute;
    top: 148px;
    left: 108px;
    display: flex;
    align-items: center;
    gap: 24px;
  }
  .brand-square { width: 72px; height: 72px; background: var(--badge-red); }
  .brand-name {
    font-family: "Tinos", serif;
    font-weight: 400;
    color: var(--ink);
    font-size: 40px;
    line-height: 1.2;
  }
  .keywords {
    position: absolute;
    top: 296px;
    left: 0;
    width: 848px;
    text-align: center;
    font-family: "Sniglet", sans-serif;
    font-weight: 800;
    font-size: 42px;
    line-height: 50px;
    text-transform: uppercase;
    letter-spacing: 0.5px;
    -webkit-text-stroke: 4px var(--ink);
    paint-order: stroke fill;
    text-shadow: 2px 3px 0 rgba(0,0,0,.6);
  }
  .keywords span { display: block; }
  .keywords .line-one { color: var(--line-yellow); }
  .keywords .line-two { color: var(--line-blue); }
  .keywords .line-three { color: var(--line-red); }
</style>
</head>
<body>
<main class="poster">
  <div class="wash" role="img" aria-label="Student watercolour painting in rainbow tones with silhouettes of children holding hands"></div>
  <div class="heart-art" role="img" aria-label="Student drawing of a large patterned blue heart"></div>
  <header class="badge">
    <span class="word-building">Building</span>
    <span class="word-block">Block</span>
    <span class="word-number">#2</span>
  </header>
  <div class="brand">
    <div class="brand-square"></div>
    <div class="brand-name">Harbor Learning Center<br>for Growth and Discovery</div>
  </div>
  <h1 class="keywords">
    <span class="line-one">Students are friends</span>
    <span class="line-two">with each other, and welcome</span>
    <span class="line-three">new students with open arms.</span>
  </h1>
</main>
</body>
</html>
```